Hi, Looking for an upgraded business card to the aged one attached. Open to suggestions and no real limitations, but if your going to use a picture of a taxi i think it should be vector based rather than a full color picture. I've uploaded a 2 pictures of the type of taxi which is a Torvane K5 in white. The taxi markings look like the pink one in the picture but to be clear his is white. The taxi is in Bermuda so if you wanted to include something island based that's ok as well but not required. The other thing he wanted to keep on there was the Harbour Police Service, with the retired police office incorporated somehow.

Requirements
Must have
• Bermuda Taxi Operator
Retired Police Officer
Police Crest
Taxi #
Email
Mobile Number

```html
<!DOCTYPE html>
<html lang="en">
<head>
<meta charset="utf-8">
<title>Bermuda Taxi Operator – Business Card</title>
<link rel="stylesheet" href="https://fonts.googleapis.com/css2?family=Lato:wght@300;400;700;900&display=swap">
<style>
  :root {
    --bg: #d9d9d9;
    --card: #ffffff;
    --ink: #111111;
    --ink-mid: #3a3a3a;
    --ink-soft: #6b6b6b;
    --crest: #3c3c3c;
  }
  * { box-sizing: border-box; margin: 0; padding: 0; }
  html, body {
    width: 1200px; height: 807px; overflow: hidden;
    background: var(--bg);
    font-family: "Lato", Arial, sans-serif;
  }
  .stage {
    width: 1200px; height: 807px;
    display: flex; align-items: center; justify-content: center;
  }
  .card {
    position: relative;
    width: 760px; height: 440px;
    background: var(--card);
    border-radius: 26px;
    box-shadow: 0 10px 30px rgba(0,0,0,0.12);
  }
  .card__title {
    position: absolute; left: 52px; top: 48px;
    font-weight: 900; font-size: 44px; letter-spacing: 0.5px;
    color: var(--ink);
  }
  .contact {
    position: absolute; left: 52px; bottom: 56px;
  }
  .contact__name {
    font-weight: 700; font-size: 22px; color: var(--ink-mid);
  }
  .contact__role {
    font-weight: 300; font-size: 19px; color: var(--ink-soft);
    margin-top: 2px;
  }
  .contact__list { list-style: none; margin-top: 22px; }
  .contact__item {
    display: flex; align-items: center; gap: 10px;
    font-weight: 300; font-size: 18px; color: var(--ink-soft);
    line-height: 1.5;
  }
  .contact__icon { width: 16px; height: 16px; flex: none; }
  .crest {
    position: absolute; left: 410px; top: 150px;
    display: flex; flex-direction: column; align-items: center; gap: 12px;
    width: 190px;
  }
  .crest__mark {
    width: 120px; height: 120px; border-radius: 50%;
    background: var(--crest);
  }
  .crest__name {
    font-weight: 700; font-size: 16px; color: var(--crest);
    text-align: center; letter-spacing: 0.5px;
  }
  .taxi-number {
    position: absolute; right: 52px; bottom: 52px;
    font-weight: 400; font-size: 40px; color: var(--ink-mid);
  }
</style>
</head>
<body>
<main class="stage">
  <article class="card">
    <h1 class="card__title">BERMUDA TAXI OPERATOR</h1>

    <section class="contact">
      <p class="contact__name">Dorian Mallet</p>
      <p class="contact__role">Retired Police Officer</p>
      <ul class="contact__list">
        <li class="contact__item">
          <svg class="contact__icon" viewBox="0 0 16 16" aria-hidden="true">
            <circle cx="8" cy="8" r="8" fill="#3a3a3a"/>
            <path d="M5.2 4.2l1.4-.3.9 2-1 .8c.5 1.1 1.3 1.9 2.4 2.4l.8-1 2 .9-.3 1.4c-3.4.3-6.5-2.8-6.2-6.2z" fill="#fff"/>
          </svg>
          +1 441 555 0142
        </li>
        <li class="contact__item">
          <svg class="contact__icon" viewBox="0 0 16 16" aria-hidden="true">
            <rect x="0" y="0" width="16" height="16" rx="2" fill="#3a3a3a"/>
            <rect x="3" y="5" width="10" height="7" fill="#fff"/>
            <path d="M3 5l5 4 5-4" fill="none" stroke="#3a3a3a" stroke-width="1.2"/>
          </svg>
          dmallet22@mailbox.example
        </li>
      </ul>
    </section>

    <div class="crest">
      <span class="crest__mark"></span>
      <span class="crest__name">Harbour Police Service</span>
    </div>

    <p class="taxi-number">Taxi # T2417</p>
  </article>
</main>
</body>
</html>
```